Vértice Lunar Presentation

We already have a logo, and now we need a good presentation for our company. You can seach for us at : verticelunar.pt and see more about us. We work in adaptive reuse of buildings. You can ask anything you need to do a great job.

Industry/Entity Type

It Company

```html
<!DOCTYPE html>
<html lang="en">
<head>
<meta charset="utf-8">
<title>Vértice Lunar — Presentation Slides</title>
<link rel="stylesheet" href="https://fonts.googleapis.com/css2?family=Source+Sans+3:wght@400;600;700&display=swap">
<style>
  :root {
    --brand-blue: #3364ae;
    --brand-grey: #b3b3b3;
    --accent-yellow: #f7bf1a;
    --agenda-muted: #8fb0e6;
    --text-dark: #333333;
    --paper: #ffffff;
  }
  * { margin: 0; padding: 0; box-sizing: border-box; }
  html, body {
    width: 1200px; height: 1000px; overflow: hidden;
    background: var(--paper);
    font-family: "Source Sans 3", "Myriad Pro", sans-serif;
  }
  .canvas { position: relative; width: 1200px; height: 1000px; }
  .slide { position: absolute; }

  /* shared */
  .skyline { position: absolute; background: var(--brand-blue); }
  .rule { position: absolute; background: var(--brand-blue); }
  .band { position: absolute; background: var(--brand-blue); }
  .band-edge { position: absolute; height: 1px; background: var(--brand-blue); opacity: .6; }
  .wordmark { position: absolute; color: var(--brand-blue); font-weight: 700; white-space: nowrap; display: flex; align-items: center; }
  .wordmark .dot { display: inline-block; border-radius: 50%; background: var(--brand-blue); }

  .contact { position: absolute; color: var(--paper); }
  .contact-title { font-size: 14px; font-weight: 600; letter-spacing: -0.2px; margin-bottom: 8px; }
  .contact-list { list-style: none; }
  .contact-list li { display: flex; align-items: center; height: 18.5px; font-size: 11px; font-weight: 600; }
  .contact-list svg { width: 10px; height: 10px; margin-right: 16px; fill: var(--paper); }

  /* cover */
  .cover { left: 16px; top: 0; width: 567px; height: 472px; }
  .cover .wordmark { left: 0; width: 567px; top: 130px; justify-content: center; font-size: 40px; letter-spacing: -0.5px; }
  .cover .wordmark .dot { width: 30px; height: 30px; margin-right: 12px; }
  .cover .skyline { left: 96px; top: 268px; width: 368px; height: 70px; }
  .cover .rule { left: 0; top: 338px; width: 567px; height: 5px; }
  .cover .band { left: 0; top: 347px; width: 567px; height: 123px; }
  .cover .band-edge { left: 0; top: 471px; width: 567px; }
  .cover .contact { left: 401px; top: 372px; }

  /* content slide */
  .content { left: 628px; top: 0; width: 565px; height: 472px; }
  .content .header { position: absolute; left: 25px; top: 59px; color: var(--brand-blue); font-size: 21px; font-weight: 700; letter-spacing: -0.5px; line-height: 1; }
  .content .subheader { position: absolute; left: 25px; top: 82px; color: var(--brand-grey); font-size: 18px; font-weight: 700; letter-spacing: -0.2px; line-height: 1; }
  .content .wordmark { right: 42px; top: 68px; font-size: 14px; }
  .content .wordmark .dot { width: 10px; height: 10px; margin-right: 5px; }
  .content .header-rule { position: absolute; left: 445px; top: 104px; width: 120px; height: 1px; background: linear-gradient(to right, rgba(51,100,174,0), var(--brand-blue)); }
  .content .body-text { position: absolute; left: 25px; top: 133px; color: var(--text-dark); font-size: 18px; letter-spacing: -0.4px; }
  .content .skyline { left: 345px; top: 398px; width: 177px; height: 35px; }
  .content .rule { left: 0; top: 432px; width: 565px; height: 2px; }
  .content .band { left: 0; top: 436px; width: 565px; height: 36px; }
  .agenda { position: absolute; left: 0; top: 436px; width: 565px; height: 36px; display: flex; align-items: center; list-style: none; }
  .agenda li { position: relative; font-size: 11px; color: var(--agenda-muted); text-transform: uppercase; margin-left: 28px; }
  .agenda li:first-child { margin-left: 28px; }
  .agenda li.is-active { color: var(--paper); font-weight: 700; font-size: 12px; }
  .agenda li.is-active::before { content: ""; position: absolute; left: -2px; right: -2px; top: -12px; height: 3px; background: var(--accent-yellow); }
  .page-number { position: absolute; right: 12px; top: 446px; color: var(--accent-yellow); font-size: 14px; font-weight: 700; }

  /* closing */
  .closing { left: 16px; top: 490px; width: 567px; height: 470px; }
  .closing .skyline { left: 96px; top: 100px; width: 368px; height: 72px; }
  .closing .rule { left: 0; top: 172px; width: 567px; height: 5px; }
  .closing .band { left: 0; top: 181px; width: 567px; height: 287px; }
  .closing .band-edge { left: 0; top: 468px; width: 567px; }
  .closing-message { position: absolute; left: 0; width: 567px; top: 203px; text-align: center; color: var(--paper); font-size: 20px; font-weight: 600; letter-spacing: -0.5px; }
  .question-mark { position: absolute; left: 404px; top: 232px; color: var(--accent-yellow); font-size: 120px; line-height: 1; }
  .closing .contact { left: 401px; top: 369px; }
</style>
</head>
<body>
<div class="canvas">

  <svg width="0" height="0" style="position:absolute">
    <defs>
      <symbol id="icon-pin" viewBox="0 0 10 10"><path d="M5 0a3.3 3.3 0 0 0-3.3 3.3C1.7 5.8 5 10 5 10s3.3-4.2 3.3-6.7A3.3 3.3 0 0 0 5 0zm0 4.6a1.3 1.3 0 1 1 0-2.6 1.3 1.3 0 0 1 0 2.6z"/></symbol>
      <symbol id="icon-mail" viewBox="0 0 10 10"><path d="M0 2h10v6H0z M.6 2.4 5 5.6l4.4-3.2" fill="none" stroke="#fff" stroke-width="1"/></symbol>
      <symbol id="icon-phone" viewBox="0 0 10 10"><path d="M2.2.5 3.6 2.8 2.7 3.8c.7 1.5 1.8 2.7 3.4 3.5l1-.9L9.5 7.8 8.4 9.5C4.2 9.1.9 5.7.5 1.6z"/></symbol>
    </defs>
  </svg>

  <!-- Cover slide -->
  <section class="slide cover">
    <div class="wordmark"><span class="dot"></span>Vértice Lunar</div>
    <div class="skyline" role="img" aria-label="Blue city skyline illustration with a house and buildings"></div>
    <div class="rule"></div>
    <div class="band"></div>
    <div class="band-edge"></div>
    <div class="contact">
      <p class="contact-title">Contact:</p>
      <ul class="contact-list">
        <li><svg><use href="#icon-pin"/></svg>Address</li>
        <li><svg><use href="#icon-mail"/></svg>Email</li>
        <li><svg><use href="#icon-phone"/></svg>Phone #</li>
      </ul>
    </div>
  </section>

  <!-- Content slide -->
  <section class="slide content">
    <h1 class="header">Header</h1>
    <h2 class="subheader">SUBHEADER</h2>
    <div class="wordmark"><span class="dot"></span>Vértice Lunar</div>
    <div class="header-rule"></div>
    <p class="body-text">Here is your text</p>
    <div class="skyline" role="img" aria-label="Small blue city skyline illustration"></div>
    <div class="rule"></div>
    <div class="band"></div>
    <ul class="agenda">
      <li>Agenda 1</li>
      <li class="is-active">Agenda 2</li>
      <li>Agenda 3</li>
      <li>Agenda 4</li>
      <li>Agenda 5</li>
      <li>Agenda 6</li>
    </ul>
    <span class="page-number">2</span>
  </section>

  <!-- Closing slide -->
  <section class="slide closing">
    <div class="skyline" role="img" aria-label="Blue city skyline illustration with a house and buildings"></div>
    <div class="rule"></div>
    <div class="band"></div>
    <div class="band-edge"></div>
    <p class="closing-message">Feel free to contact us if you have any additional questions</p>
    <span class="question-mark">?</span>
    <div class="contact">
      <p class="contact-title">Contact:</p>
      <ul class="contact-list">
        <li><svg><use href="#icon-pin"/></svg>Address</li>
        <li><svg><use href="#icon-mail"/></svg>Email</li>
        <li><svg><use href="#icon-phone"/></svg>Phone #</li>
      </ul>
    </div>
  </section>

</div>
</body>
</html>
```